Book a Belle needs a Stunning web design

Book a Belle is an upmarket agency in Sydney that has lingerie waitresses for events.

Book a Belle is looking for a website design that is as sexy and sophisticated as the ladies who work for them!

The design mustn't be cluttered, tacky or pornographic. What I'm looking for is something better than the industry leader www.velvetquills.com.au Something classy, sexy and different.

When designing please suggest a CMS, we already use wordpress but are open to suggestions.

We will need a home page that incorporates a feed from a blog and/or social media (please make suggestions and use your discretion as a designer, however we'd like to approve what goes into the feed before it goes in.) The home page could also have a list of our services, but if not we will need a services page. Our Services include:
Lingerie waitressing at events
Lingerie waitresses to help dress the groom pre wedding.
Bucks parties

We have a logo that we'd like incorporated into the design and have attached it.

We will also need a portfolio page for the ladies, This is not to be cluttered, tacky or pornographic. It needs to be classy.

We will also need a "Contact us" page and were thinking that this could potentially also be a "Ask for a quote on your event" page. I.e. have a regular "Contact us" form but have alternate fields if they tick the "I want a quote" box. Alternatively you could have two parts to the contact us page. One that is a regular form and one that has a "Your requirements" box.

Again please use your discretion when designing these, if it's too cluttered it won't work. If it looks tacky, don't do it. If you have suggestions make them.

Target Market(s)

Males between the ages of 18 - 45

Industry/Entity Type

Industry

Requirements
Must have
• Must incorporate our logo.

```html
<!DOCTYPE html>
<html lang="en">
<head>
<meta charset="utf-8">
<title>Book a Belle – Lingerie Waitresses for Events</title>
<link rel="stylesheet" href="https://fonts.googleapis.com/css2?family=Comfortaa:wght@400;700&family=Delius&family=Lato:wght@400;700&display=swap">
<style>
:root{
  --mint:#a9e3cf;
  --mint-light:#d5f2e8;
  --mint-line:#b7ddd0;
  --mint-dot:#7fcfb2;
  --crimson:#d8173f;
  --plum:#4a1830;
  --ink:#2b2b2b;
  --body:#4a4a4a;
  --sand:#f2e6c9;
  --sand-edge:#d8b98a;
  --footer:#111;
  --footer-text:#d8d8d8;
  --white:#fff;
}
*{margin:0;padding:0;box-sizing:border-box}
html,body{width:993px;height:1200px;overflow:hidden;background:var(--white)}
body{position:relative;font-family:"Lato",sans-serif;color:var(--body)}
.abs{position:absolute}
.hero-band{left:0;top:0;width:993px;height:463px;background:linear-gradient(180deg,var(--mint-light) 0%,#bfe9da 45%,var(--mint) 70%,#9bdcc4 100%)}
.hero-panel{left:0;top:0}
.brand-tab{left:118px;top:10px;width:205px;height:110px;display:flex;align-items:center;justify-content:center;gap:8px;font-family:"Delius",cursive;font-size:22px;color:var(--ink)}
.brand-dot{width:10px;height:10px;border-radius:50%;background:var(--crimson)}
.social{left:608px;top:17px;display:flex;gap:12px;font-family:"Delius",cursive;font-size:12px;color:var(--ink)}
.booking{left:755px;top:9px;font-family:"Delius",cursive;color:var(--ink);font-size:15px;line-height:1.2}
.booking strong{display:flex;align-items:center;gap:4px;font-weight:400;font-size:20px;margin-left:6px}
.headline{left:153px;top:114px;font-family:"Comfortaa",sans-serif;font-weight:700;font-size:80px;color:var(--crimson);letter-spacing:-2px;line-height:1}
.subline{left:157px;top:202px;font-family:"Comfortaa",sans-serif;font-size:24px;color:var(--plum);letter-spacing:.5px}
.intro{left:158px;top:242px;width:252px;font-size:9px;line-height:11.5px;color:#555}
.btn-pill{left:154px;top:293px;width:144px;height:31px;border-radius:16px;background:linear-gradient(var(--white),var(--sand));border:1px solid var(--sand-edge);font-family:"Delius",cursive;font-size:12.5px;color:var(--ink);display:flex;align-items:center;justify-content:center}
.feature-photo{left:436px;top:113px;width:298px;height:298px;border-radius:50%;background:radial-gradient(circle at 45% 40%,#e7b98a,#a66a3e 60%,#4a2b1c);border:2px solid #eee}
.badge{left:666px;top:89px;width:92px;height:92px;border-radius:50%;background:radial-gradient(circle at 40% 35%,#ee3b5b,var(--crimson) 70%);color:var(--white);font-family:"Delius",cursive;font-size:14px;line-height:14px;text-align:center;display:flex;align-items:center;justify-content:center;box-shadow:0 2px 4px rgba(0,0,0,.2)}
.badge b{font-weight:400;font-size:17px}
.arrow{width:30px;height:30px;border-radius:50%;background:linear-gradient(var(--white),var(--sand));border:1px solid var(--sand-edge);display:flex;align-items:center;justify-content:center}
.model-card{left:603px;top:345px;width:152px;height:152px;border-radius:50%;background:linear-gradient(var(--white),var(--sand));border:2px solid #e6cfa4;text-align:center;padding-top:22px}
.model-card h3{font-family:"Delius",cursive;font-weight:400;font-size:26px;color:var(--ink)}
.model-card h3::after{content:"";display:block;width:120px;height:1px;background:var(--sand-edge);margin:6px auto 8px}
.model-card p{font-size:9.5px;line-height:11.5px;color:#444;padding:0 22px}
.model-card .book{display:inline-block;margin-top:9px;background:var(--crimson);color:var(--white);font-size:8.5px;padding:3px 11px;border-radius:3px}
.figure-outline{left:765px;top:58px;width:110px;height:438px;border-radius:55px 55px 20px 20px;background:linear-gradient(90deg,rgba(255,255,255,.1),rgba(255,255,255,.35),rgba(255,255,255,.1))}
.hanger{width:2px;background:var(--mint-dot)}
.hanger::before,.hanger::after{content:"";position:absolute;left:-4px;width:10px;height:10px;border-radius:50%;border:2px solid var(--mint-dot);background:var(--white)}
.hanger::before{top:-4px}.hanger::after{bottom:-4px}
.box{background:var(--white);border:1px solid var(--mint-line)}
.box-title{font-family:"Delius",cursive;font-weight:400;color:var(--ink);font-size:26px;padding:16px 0 8px 21px;border-bottom:1px solid var(--mint-line);position:relative}
.box-title::after{content:"";position:absolute;right:8px;top:6px;width:9px;height:44px;border-radius:5px;background:var(--mint)}
.services{left:118px;top:412px;width:240px;height:222px}
.services .box-title{width:190px}
.service-list{list-style:none;padding:4px 0 0 25px}
.service-list li{font-size:11px;color:#333;height:25px;display:flex;align-items:center;gap:10px}
.service-list li::before{content:"‹";width:11px;height:11px;border-radius:50%;background:var(--mint-dot);color:var(--white);font-size:10px;line-height:10px;text-align:center}
.top-models{left:118px;top:654px;width:240px;height:254px}
.top-models .box-title{width:194px}
.model-thumb{left:27px;top:70px;width:184px;height:144px;border:1px solid var(--mint-line);padding:3px}
.model-thumb div{width:100%;height:100%;background:linear-gradient(135deg,#f2eee9,#c9a48a 55%,#3a2a25)}
.model-name{left:0;top:220px;width:240px;text-align:center;font-family:"Delius",cursive;font-size:19px;color:var(--ink)}
.side-arrow{width:26px;height:30px;background:linear-gradient(var(--white),var(--mint-light));border:1px solid var(--mint-line);display:flex;align-items:center;justify-content:center}
.welcome{left:386px;top:500px;font-family:"Delius",cursive;font-weight:400;font-size:28px;color:var(--ink)}
.welcome em{font-style:normal;color:var(--crimson);font-size:36px}
.welcome-rule{left:386px;top:556px;width:380px;height:1px;background:var(--mint-line)}
.welcome-copy{left:388px;top:576px;width:490px;font-size:8.8px;line-height:15px;color:#444}
.welcome-copy p+p{margin-top:7px}
.media{left:386px;top:695px;width:497px;height:232px}
.media .box-title{width:194px;padding-top:14px}
.media-photo{left:16px;top:71px;width:184px;height:145px;border:1px solid var(--mint-line);padding:3px}
.media-photo div{width:100%;height:100%;background:linear-gradient(90deg,#e7c7b0,#8a5a45 45%,#f1e2cf 70%,#caa07f)}
.media-copy{left:227px;top:70px;width:252px;font-size:8.8px;line-height:15px;color:#444}
.media-copy p+p{margin-top:15px}
.read-more{display:block;margin-top:16px;color:var(--crimson);font-weight:700;font-size:8.8px}
.footer{left:0;top:952px;width:993px;height:248px;background:linear-gradient(#2a2a2a,var(--footer) 30%)}
.footer-brand{left:149px;top:1030px;display:flex;align-items:center;gap:10px;font-family:"Delius",cursive;font-size:30px;color:var(--crimson)}
.footer-brand span.mark{width:12px;height:12px;border-radius:50%;background:var(--crimson)}
.copyright{left:140px;top:1107px;font-size:8.8px;color:var(--footer-text)}
.footer-title{font-family:"Delius",cursive;font-weight:400;font-size:19px;color:var(--white);padding-bottom:9px;border-bottom:1px solid #444;position:relative}
.footer-title::after{content:"";position:absolute;right:2px;top:-8px;width:8px;height:46px;border-radius:4px;background:#444}
.links{left:387px;top:982px;width:245px}
.link-cols{display:flex;gap:60px;margin-top:16px}
.link-cols ul{list-style:none}
.link-cols li{font-size:8.8px;color:var(--footer-text);height:15px}
.link-cols li::before{content:"‹";color:var(--crimson);margin-right:7px}
.events{left:669px;top:982px;width:192px}
.event{margin-top:14px;font-size:8.8px;line-height:12px;color:var(--footer-text)}
.event+.event{margin-top:11px}
.event time{display:block;color:var(--crimson)}
</style>
</head>
<body>

<div class="abs hero-band"></div>
<svg class="abs hero-panel" width="993" height="463" viewBox="0 0 993 463" aria-hidden="true">
  <path d="M118 120 A103 103 0 0 1 322 95 L815 66 L835 150 L780 445 L118 333 Z" fill="#fff"/>
</svg>

<div class="abs brand-tab"><span class="brand-dot"></span>Book a Belle</div>

<nav class="abs social" aria-label="Social links"><span>Tweets</span><span>Videos</span><span>Friends</span></nav>
<div class="abs booking">Call for bookings
  <strong><svg width="12" height="15" viewBox="0 0 12 15"><path d="M3 1 L5 4 L4 6 Q5 9 7.5 11 L9.5 10 L11.5 12.5 L9.5 14 Q3 12 1 3 Z" fill="#2b2b2b"/></svg>960318xx</strong>
</div>

<h1 class="abs headline">lingerie</h1>
<div class="abs subline">waitresses for Events</div>
<p class="abs intro">Lorem ipsum dolor sit amet, consectetuer adipiscing elit, sed diam nonummy nibh euismod tincidunt ut laoreet dolore magna aliquam...</p>
<a class="abs btn-pill">Meet the Belles</a>

<div class="abs figure-outline" role="img" aria-label="Faint outline of a standing woman in lingerie"></div>
<div class="abs feature-photo" role="img" aria-label="Featured model portrait"></div>
<div class="abs badge"><span>Select the<br>beauties<br><b>You like</b></span></div>
<div class="abs arrow" style="left:420px;top:337px"><svg width="10" height="12"><path d="M3 2 L7 6 L3 10" stroke="#c8a062" stroke-width="2.4" fill="none"/></svg></div>
<div class="abs arrow" style="left:403px;top:355px"><svg width="10" height="12"><path d="M7 2 L3 6 L7 10" stroke="#c8a062" stroke-width="2.4" fill="none"/></svg></div>
<div class="abs model-card">
  <h3>Sienna</h3>
  <p>Lorem ipsum dolor sit amet, consectetuer adipiscing elit</p>
  <span class="book">Book Now</span>
</div>

<div class="abs hanger" style="left:133px;top:335px;height:86px"></div>
<div class="abs hanger" style="left:340px;top:366px;height:55px"></div>

<section class="abs box services">
  <h2 class="box-title">Our Services</h2>
  <ul class="service-list">
    <li>lingerie waitressing</li>
    <li>bucks nights</li>
    <li>party bus tours</li>
    <li>pub crawls</li>
    <li>harbor cruises</li>
    <li>topless poker</li>
  </ul>
</section>

<section class="abs box top-models">
  <h2 class="box-title">Top Models</h2>
  <div class="abs model-thumb"><div role="img" aria-label="Model photo in black lingerie"></div></div>
  <div class="abs model-name">Lena</div>
  <div class="abs side-arrow" style="left:-1px;top:123px;border-radius:0 15px 15px 0"><svg width="8" height="10"><path d="M6 1 L2 5 L6 9" stroke="#333" stroke-width="2" fill="none"/></svg></div>
  <div class="abs side-arrow" style="right:-1px;top:123px;border-radius:15px 0 0 15px"><svg width="8" height="10"><path d="M2 1 L6 5 L2 9" stroke="#333" stroke-width="2" fill="none"/></svg></div>
</section>

<h2 class="abs welcome">Welcome to <em>Book a Belle</em></h2>
<div class="abs welcome-rule"></div>
<div class="abs welcome-copy">
  <p>Duis autem vel eum iriure dolor in hendrerit in vulputate velit esse molestie consequat, vel illum dolore eu feugiat nulla facilisis at vero eros et accumsan et iusto odio dignissim qui blandit praesent luptatum zzril delenit augue duis dolore te feugait nulla facilisi. Nam liber tempor cum soluta nobis eleifend option congue nihil imperdiet doming id quod mazim placerat facer possim assum.</p>
  <p>Typi non habent claritatem insitam; est usus legentis in iis qui facit eorum claritatem. Investigationes demonstraverunt lectores legere me ...</p>
</div>

<section class="abs box media">
  <h2 class="box-title">Media News</h2>
  <div class="abs media-photo"><div role="img" aria-label="Two models posing in lingerie"></div></div>
  <div class="abs media-copy">
    <p>Duis autem vel eum iriure dolor in hendrerit in vulputate velit esse molestie consequat, vel illum dolore eu feugiat nulla facilisis at vero eros et accumsan et iusto odio dignissim qui blandit praesent luptatum zzril delenit augue duis dolore te feugait nulla facilisi.</p>
    <p>Nam liber tempor cum soluta nobis eleifend option congue nihil imperdiet doming id quod mazim placerat facer possim assum.</p>
    <a class="read-more">Read More..</a>
  </div>
</section>

<footer class="abs footer"></footer>
<div class="abs footer-brand"><span class="mark"></span>Book a Belle</div>
<div class="abs copyright">©2012 BOOK A BELLE ALL RIGHTS RESERVED</div>

<div class="abs links">
  <h3 class="footer-title">Helpful links</h3>
  <div class="link-cols">
    <ul><li>Ut wisi enim ad</li><li>minim veniam</li><li>quis nostrud</li><li>exerci tation</li><li>ullamcorper</li><li>suscipit lobortis</li><li>nisl ut aliquip</li><li>ex ea commodo</li><li>consequat.</li></ul>
    <ul><li>Ut wisi enim ad</li><li>minim veniam</li><li>quis nostrud</li><li>exerci tation</li><li>ullamcorper</li><li>suscipit lobortis</li><li>nisl ut aliquip</li><li>ex ea commodo</li><li>consequat.</li></ul>
  </div>
</div>

<div class="abs events">
  <h3 class="footer-title">Up Coming Events</h3>
  <div class="event"><time>16-October-2012</time>Ut wisi enim ad minim veniam, quis nostrud exerci tation ullamcorper suscipit lobortis nisl ut aliquip ex ea commodo consequat.</div>
  <div class="event"><time>18-October-2012</time>Ut wisi enim ad minim veniam, quis nostrud exerci tation ullamcorper suscipit lobortis nisl ut aliquip ex ea commodo consequat.</div>
  <div class="event"><time>26-October-2012</time>Ut wisi enim ad minim veniam, quis nostrud exerci tation ullamcorper s</div>
</div>

</body>
</html>
```